Home Maintenance Business needs a logo design

I need a logo design for my start up home maintenance (home handyman) business. I will be doing basic home services like painting, yard work, plumbing, electrical, odd jobs, light building (shelving), cleaning, changing light bulbs. No job too big or small. I live in a beach area and I need a logo as well. I want some color. My idea is a beach umbrella with a ladder and tools under it???

Home Improvement

Business name: Cedar Nest Services

Sans Serif

• Scope of services: painting, gutter cleaning, yard work, plumbing, electrical, odd jobs, cleaning handyman services, no job to small
• email address: cedarnestservices@mailvora.net
• phone: 802-617-4920
• colorful card/I live in a beach community/logo with beachy feel yet explain the business

```html
<!DOCTYPE html>
<html lang="en">
<head>
<meta charset="utf-8">
<title>Cedar Nest Services – Business Card</title>
<link rel="stylesheet" href="https://fonts.googleapis.com/css2?family=Open+Sans:wght@400;600;700&display=swap">
<style>
  :root {
    --bg: #ecebe8;
    --card: #ffffff;
    --brand: #9b1b6e;
    --text: #4a4a4a;
    --muted: #6b6b6b;
    --rule: #d9d9d9;
    --palm: #7cc242;
    --sun: #f5a623;
    --tool: #e2312f;
  }
  * { margin: 0; padding: 0; box-sizing: border-box; }
  html, body { width: 1200px; height: 900px; overflow: hidden; }
  body {
    background: var(--bg);
    font-family: "Open Sans", Arial, sans-serif;
    color: var(--text);
    position: relative;
  }
  .card {
    position: absolute;
    width: 630px;
    height: 360px;
    background: var(--card);
    box-shadow: 0 6px 18px rgba(0,0,0,0.12);
  }
  .card--front { left: 150px; top: 50px; }
  .card--back  { left: 420px; top: 480px; }

  .logo-art {
    display: block;
    border-radius: 50% 50% 40% 40% / 60% 60% 30% 30%;
    background: linear-gradient(100deg, var(--palm) 0%, var(--palm) 30%, var(--tool) 48%, var(--sun) 68%, var(--brand) 88%);
    opacity: 0.85;
  }
  .logo-name {
    font-weight: 600;
    color: var(--brand);
    white-space: nowrap;
    letter-spacing: 0.5px;
  }

  /* front */
  .front-logo {
    position: absolute;
    left: 0; right: 0; top: 40px;
    display: flex; flex-direction: column; align-items: center;
  }
  .front-logo .logo-art { width: 250px; height: 100px; }
  .front-logo .logo-name { font-size: 38px; margin-top: 14px; }
  .services {
    position: absolute;
    left: 0; right: 0; bottom: 50px;
    text-align: center;
    font-size: 17px;
    line-height: 1.5;
    color: var(--muted);
  }

  /* back */
  .back-logo {
    position: absolute;
    left: 26px; top: 100px; width: 270px;
    display: flex; flex-direction: column; align-items: center;
  }
  .back-logo .logo-art { width: 190px; height: 76px; }
  .back-logo .logo-name { font-size: 24px; margin-top: 12px; }
  .divider {
    position: absolute;
    left: 318px; top: 70px;
    width: 1px; height: 200px;
    background: var(--rule);
  }
  .contact {
    position: absolute;
    left: 340px; top: 64px;
  }
  .contact__name {
    font-size: 24px; font-weight: 700; color: var(--brand);
    margin-bottom: 18px; margin-left: 10px;
  }
  .contact__address {
    font-size: 15px; line-height: 1.4; margin-left: 14px; margin-bottom: 16px;
  }
  .contact__line {
    display: flex; align-items: center; gap: 10px;
    font-size: 16px; margin-bottom: 12px;
  }
  .contact__line svg { width: 14px; height: 14px; flex: none; fill: var(--brand); }
</style>
</head>
<body>

<section class="card card--front">
  <div class="front-logo">
    <span class="logo-art" role="img" aria-label="Beach illustration: palm tree, red toolbox and striped beach umbrella on sand"></span>
    <span class="logo-name">Cedar Nest Services</span>
  </div>
  <p class="services">
    Painting, Gutter Cleaning, Yard Work, Plumbing, Electrical,<br>
    Odd Jobs, Cleaning Handyman Services, No job to small
  </p>
</section>

<section class="card card--back">
  <div class="back-logo">
    <span class="logo-art" role="img" aria-label="Beach illustration: palm tree, red toolbox and striped beach umbrella on sand"></span>
    <span class="logo-name">Cedar Nest Services</span>
  </div>
  <div class="divider"></div>
  <div class="contact">
    <p class="contact__name">Dan Whitaker</p>
    <p class="contact__address">4218 Dune Heron Lane<br>Saltmarsh Bay, SC 29599</p>
    <p class="contact__line">
      <svg viewBox="0 0 16 16" aria-hidden="true"><path d="M3.6 1.5l2.3 2.6-1.3 1.8c.9 2 2.5 3.6 4.5 4.5l1.8-1.3 2.6 2.3-1.3 2.4C7 13.6 2.4 9 2.2 3z"/></svg>
      802-617-4920
    </p>
    <p class="contact__line">
      <svg viewBox="0 0 16 16" aria-hidden="true"><path d="M1 3h14v10H1z"/><path d="M2 4.5l6 4.5 6-4.5" stroke="#fff" stroke-width="1.2" fill="none"/></svg>
      cedarnestservices@mailvora.net
    </p>
    <p class="contact__line">
      <svg viewBox="0 0 16 16" aria-hidden="true"><circle cx="8" cy="8" r="7"/><path d="M1 8h14M8 1c-3 3.5-3 10.5 0 14M8 1c3 3.5 3 10.5 0 14" stroke="#fff" stroke-width="1.1" fill="none"/></svg>
      www.cedarnestservices.net
    </p>
  </div>
</section>

</body>
</html>
```